Flyer for the Radiant Harvest Worship Day 2020

I am looking to create a flyer for a one day prayer retreat our church is organizing.
This flyer will be posted on social media, websites and will also be printed so it can be mailed to people.
I am looking for something professional, with good use of our logo and band colors (logo colors).
I am counting on the designer's skill, creativity, art and knowledge of media communication to produce a flyer that will effectively and quickly convey the message we are trying to spread.
CONTENT OF THE FLYER:
Event title: Radiant Harvest Worship Day
Date: Tuesday July 2nd, 2020
Time: 11:00AM - 7:00PM
Maplewood Hotel, 4817 Birchfield Avenue, Portland, Maine 04109 (Room: Evergreen)
Event Key words to highlight what the event is about: Prayer, Sharing the Word, Panel discussion, prophecy, Impartation.
Key phrases:
A one day prayer retreat.
Jesus Chris is Lord
Contact info:
www.tolvex.org
Phone: 207 555 0143
Email: contact@brookmeadow.org

```html
<!DOCTYPE html>
<html lang="en">
<head>
<meta charset="utf-8">
<title>Radiant Harvest Worship Day 2020</title>
<link href="https://fonts.googleapis.com/css2?family=Montserrat:wght@600;700;800;900&family=Oswald:wght@500;600&family=Mrs+Saint+Delafield&display=swap" rel="stylesheet">
<style>
  :root {
    --page: #ffffff;
    --ink-black: #000000;
    --navy-deep: #031d33;
    --navy: #022a4a;
    --orange: #f7941d;
    --white: #ffffff;
    --sky-dark: #2a0d12;
    --sky-red: #7a2a22;
    --sky-glow: #f0b25a;
    --skin: #c9905e;
  }
  * { margin: 0; padding: 0; box-sizing: border-box; }
  html, body { width: 1200px; height: 843px; overflow: hidden; background: var(--page); }
  .flyer {
    position: absolute; left: 311px; top: 46px; width: 580px; height: 751px; overflow: hidden;
    background: linear-gradient(to bottom, var(--ink-black) 0%, var(--ink-black) 52%, var(--navy-deep) 82%, var(--navy) 100%);
    color: var(--white); font-family: "Montserrat", sans-serif;
  }
  .sky-photo {
    position: absolute; left: 0; top: 0; width: 580px; height: 185px;
    background:
      radial-gradient(ellipse 130px 90px at 260px 60px, var(--sky-glow) 0%, rgba(208,110,50,.7) 40%, rgba(0,0,0,0) 100%),
      linear-gradient(to bottom, var(--sky-dark) 0%, var(--sky-red) 45%, rgba(60,20,15,.8) 75%, var(--ink-black) 100%);
  }
  .hands-photo {
    position: absolute; left: 154px; top: 145px; width: 265px; height: 194px;
    background: radial-gradient(ellipse 110px 90px at 50% 50%, var(--skin) 0%, rgba(140,90,50,.75) 55%, rgba(0,0,0,0) 100%);
  }
  .brand { position: absolute; left: 437px; top: 48px; display: flex; align-items: center; gap: 6px; }
  .brand-dot { width: 12px; height: 12px; border-radius: 50%; background: var(--orange); }
  .brand-name { font-weight: 700; font-size: 22px; color: var(--white); letter-spacing: 1px; }
  .title { display: block; position: absolute; left: 0; width: 580px; text-align: center; font-weight: 900; line-height: 1; }
  .title-top { top: 351px; font-size: 40px; color: var(--white); }
  .title-main { top: 386px; font-size: 52px; color: var(--orange); letter-spacing: 1px; }
  .title-rule {
    position: absolute; left: 92px; top: 438px; width: 395px; height: 2px;
    background: linear-gradient(to right, rgba(255,255,255,0), var(--white) 20%, var(--white) 80%, rgba(255,255,255,0));
  }
  .tagline {
    position: absolute; left: 0; top: 442px; width: 580px; text-align: center;
    font-weight: 800; font-size: 16px; letter-spacing: 3px; line-height: 1;
  }
  .confession {
    position: absolute; left: 0; top: 466px; width: 580px; text-align: center;
    font-family: "Mrs Saint Delafield", cursive; font-size: 34px; line-height: 34px; color: var(--white);
  }
  .event-box {
    position: absolute; left: 73px; top: 519px; width: 437px; height: 72px;
    border: 2px solid var(--white); border-radius: 9px;
  }
  .date-day, .date-month, .date-year { position: absolute; font-family: "Oswald", sans-serif; font-weight: 600; line-height: 1; transform-origin: left top; white-space: nowrap; }
  .date-day { left: 11px; top: 3px; font-size: 34px; transform: scaleX(.8); }
  .date-month { left: 24px; top: 34px; font-size: 28px; color: var(--orange); transform: scaleX(.78); }
  .date-year { left: 102px; top: -2px; font-size: 66px; transform: scaleX(.78); }
  .date-divider { position: absolute; left: 214px; top: 8px; width: 2px; height: 53px; background: var(--orange); }
  .time-tag {
    position: absolute; left: 231px; top: 8px; height: 17px; padding: 0 5px;
    background: var(--white); color: var(--ink-black); white-space: nowrap;
    font-family: "Oswald", sans-serif; font-weight: 500; font-size: 15px; line-height: 17px;
    transform: scaleX(.85); transform-origin: left top;
  }
  .venue { position: absolute; left: 231px; top: 29px; font-size: 9.5px; font-weight: 700; line-height: 10.5px; white-space: nowrap; }
  .keywords { position: absolute; left: 0; width: 580px; display: flex; justify-content: center; font-weight: 700; font-size: 13px; }
  .keywords span { padding: 0 7px; line-height: 23px; }
  .keywords span + span { border-left: 2px solid var(--orange); }
  .keywords-one { top: 609px; }
  .keywords-two { top: 636px; }
  .contact-band {
    position: absolute; left: 0; top: 680px; width: 580px; height: 47px; background: var(--orange);
    color: var(--navy); font-weight: 700; font-size: 12px;
  }
  .contact-icon { position: absolute; top: 50%; transform: translateY(-50%); }
  .contact-text { position: absolute; top: 0; line-height: 47px; white-space: nowrap; }
  .phone-icon { left: 36px; }
  .phone-text { left: 75px; font-size: 13px; }
  .mail-icon { left: 188px; }
  .mail-text { left: 226px; }
  .web-icon { left: 408px; }
  .web-text { left: 445px; }
  .footer-band { position: absolute; left: 0; top: 727px; width: 580px; height: 24px; background: var(--navy); }
</style>
</head>
<body>
<main class="flyer">
  <div class="sky-photo" role="img" aria-label="Dramatic sunset sky with sunlight breaking through red clouds"></div>
  <div class="hands-photo" role="img" aria-label="Clasped hands in prayer holding a small cross"></div>

  <div class="brand">
    <span class="brand-dot"></span>
    <span class="brand-name">TOLVEX</span>
  </div>

  <h1>
    <span class="title title-top">RADIANT HARVEST</span>
    <span class="title title-main">WORSHIP DAY</span>
  </h1>
  <div class="title-rule"></div>
  <p class="tagline">A ONE DAY PRAYER RETREAT</p>
  <p class="confession">Jesus Chris is Lord</p>

  <section class="event-box">
    <span class="date-day">TUESDAY</span>
    <span class="date-month">JULY 2ND</span>
    <span class="date-year">2020</span>
    <span class="date-divider"></span>
    <span class="time-tag">11:00AM - 7:00PM</span>
    <p class="venue">Maplewood Hotel, 4817 Birchfield<br>Avenue, Portland, Maine 04109<br>(Room: Evergreen)</p>
  </section>

  <div class="keywords keywords-one"><span>SHARING THE WORD</span><span>PRAYER</span><span>PANEL DISCUSSION</span></div>
  <div class="keywords keywords-two"><span>PROPHECY</span><span>IMPARTATION</span></div>

  <footer class="contact-band">
    <svg class="contact-icon phone-icon" width="29" height="29" viewBox="0 0 30 30" fill="none" stroke="#022a4a" stroke-width="2">
      <circle cx="15" cy="15" r="13.5"/>
      <path d="M10 8.5l3 0 1.2 3.5-2 1.5c.9 2 2.3 3.4 4.3 4.3l1.5-2 3.5 1.2v3c-6.5.6-12-4.9-11.5-11.5z" fill="#022a4a"/>
    </svg>
    <span class="contact-text phone-text">207 555 0143</span>
    <svg class="contact-icon mail-icon" width="30" height="22" viewBox="0 0 30 22" fill="none" stroke="#022a4a" stroke-width="2">
      <rect x="1" y="1" width="28" height="20" rx="1"/>
      <path d="M1 1l14 11L29 1M1 21l10-9M29 21l-10-9"/>
    </svg>
    <span class="contact-text mail-text">contact@brookmeadow.org</span>
    <svg class="contact-icon web-icon" width="29" height="29" viewBox="0 0 30 30" fill="none" stroke="#022a4a" stroke-width="1.8">
      <circle cx="15" cy="15" r="13.5"/>
      <ellipse cx="15" cy="15" rx="6" ry="13.5"/>
      <path d="M15 1.5v27M1.5 15h27M3.5 8h23M3.5 22h23"/>
    </svg>
    <span class="contact-text web-text">www.tolvex.org</span>
  </footer>
  <div class="footer-band"></div>
</main>
</body>
</html>
```